My Peace sticker-empathy for others is peace

i want a Peace sticker.... with a dove (with an olive branch in its beak) and the words:

EMPATHY FOR OTHERS IS PEACE

2 INCH X 2 INCH SQUARE STICKER

2 color design

Font style is important to me....

A 20 sticker pack of "Lumen Dots" is going to be handed out to the people who come to my funeral... and will be given to a synagogue .. for them to sell in their gift shop... the proceeds will go to a camp fund in my father's name that funds kids who can not afford to go to summer camp.

I bought Lumen Dots in a packet 10 years ago... and put them on all of the cards and letters i sent to others...

yes before emails... and texts....we actually sent cards and letters in the mail to other human beings.

I have worked with battered women for 20 years... and believe in Peace....

I believe that Peace is not possible without EMPATHY.

Target Market(s)

people who come to my funeral... people who are interested in peace will buy these stickers.

Font styles to use
Decorative

Colors
e34197
ec1f27
6b449b
ffffff

Requirements
Must have
• i would like to see some kind of a border....an interesting font style..
Should not have
• i do not like the color green

```html
<!DOCTYPE html>
<html lang="en">
<head>
<meta charset="utf-8">
<title>Empathy for Others is Peace – Sticker</title>
<link href="https://fonts.googleapis.com/css2?family=Arvo:wght@700&family=Kreon:wght@500;700&family=Arimo:wght@400&display=swap" rel="stylesheet">
<style>
  :root {
    --paper: #ffffff;
    --frame-grey: #636161;
    --ink-grey: #5f5d5d;
    --peace-red: #e0241f;
    --hairline: #e2e2e2;
    --caption-ink: #1a1a1a;
  }
  * { margin: 0; padding: 0; box-sizing: border-box; }
  html, body {
    width: 1200px;
    height: 1200px;
    overflow: hidden;
    background: var(--paper);
  }
  .canvas {
    position: relative;
    width: 1200px;
    height: 1200px;
    background: var(--paper);
  }
  .sticker {
    position: absolute;
    left: 360px;
    top: 360px;
    width: 480px;
    height: 480px;
    border: 1px solid var(--hairline);
    background: var(--paper);
  }
  .sticker__frame {
    position: absolute;
    left: 22px;
    top: 22px;
    width: 435px;
    height: 434px;
    border: 18px solid var(--frame-grey);
  }
  .headline {
    position: absolute;
    left: 58px;
    top: 56px;
    width: 366px;
    text-align: center;
    font-family: "Arvo", Georgia, serif;
    font-weight: 700;
    font-size: 74px;
    line-height: 1;
    color: var(--ink-grey);
    letter-spacing: -1px;
  }
  .dove-art {
    position: absolute;
    left: 158px;
    top: 140px;
    width: 222px;
    height: 164px;
  }
  .tagline {
    position: absolute;
    left: 112px;
    top: 314px;
    width: 320px;
    text-align: center;
    font-family: "Kreon", Georgia, serif;
    font-weight: 700;
    font-size: 44px;
    line-height: 1;
    color: var(--ink-grey);
    letter-spacing: 1px;
  }
  .tagline__accent {
    position: absolute;
    left: 146px;
    top: 364px;
    width: 250px;
    text-align: center;
    font-family: "Kreon", Georgia, serif;
    font-weight: 700;
    font-size: 82px;
    line-height: 1;
    color: var(--peace-red);
  }
  .corner-flourish {
    position: absolute;
    left: 10px;
    top: 296px;
    width: 114px;
    height: 156px;
  }
  .spec-note {
    position: absolute;
    left: 0;
    width: 1200px;
    font-family: "Arimo", Arial, sans-serif;
    font-weight: 400;
    font-size: 46px;
    line-height: 1;
    color: var(--caption-ink);
    text-align: center;
  }
  .spec-note--tone { top: 888px; left: -4px; }
  .spec-note--curves { top: 952px; left: 18px; }
</style>
</head>
<body>
  <main class="canvas">
    <section class="sticker" aria-label="Empathy for others is peace sticker">
      <div class="sticker__frame"></div>

      <h1 class="headline">Empathy</h1>

      <svg class="dove-art" role="img" aria-label="Line drawing of a dove carrying a red olive branch in its beak" viewBox="0 0 222 164">
        <defs>
          <linearGradient id="doveTone" x1="0" y1="0" x2="1" y2="0">
            <stop offset="0" stop-color="#f1f0f0"/>
            <stop offset="0.7" stop-color="#ececec"/>
            <stop offset="1" stop-color="#f6d6d5"/>
          </linearGradient>
        </defs>
        <rect x="0" y="0" width="222" height="164" rx="10" fill="url(#doveTone)"/>
      </svg>

      <p class="tagline">For others is</p>
      <p class="tagline__accent">Peace</p>

      <svg class="corner-flourish" role="img" aria-label="Grey scroll ornament with a red flower in the corner" viewBox="0 0 114 156">
        <defs>
          <linearGradient id="flourishTone" x1="0" y1="0" x2="0" y2="1">
            <stop offset="0" stop-color="#d9d8d8"/>
            <stop offset="1" stop-color="#f0c9c8"/>
          </linearGradient>
        </defs>
        <rect x="0" y="0" width="114" height="156" rx="10" fill="url(#flourishTone)"/>
      </svg>
    </section>

    <p class="spec-note spec-note--tone">70% Black</p>
    <p class="spec-note spec-note--curves">Removed Curves</p>
  </main>
</body>
</html>
```